Realty Group Needs Classy, Contemporary Letterhead Design

We need a letterhead design for a new realty company located in NY, USA. We buy investment properties to rehabilitate and or keep in our rental portfolio.

```html
<!DOCTYPE html>
<html lang="en">
<head>
<meta charset="utf-8">
<title>Halvern Realty Group – Letterhead</title>
<link href="https://fonts.googleapis.com/css2?family=Mulish:wght@400;600;700;800;900&display=swap" rel="stylesheet">
<style>
  :root {
    --backdrop: #8e8f8d;
    --paper: #ffffff;
    --brand-purple: #4b2a8c;
    --brand-blue: #1f55a8;
    --ink: #2b2b2b;
    --muted: #6b6b6b;
    --panel: #f3f3f4;
    --rule: #5a3b9a;
    --signature-tone: #e6e6ea;
  }
  * { box-sizing: border-box; margin: 0; padding: 0; }
  html, body { width: 1200px; height: 803px; overflow: hidden; }
  body {
    background: var(--backdrop);
    font-family: "Mulish", sans-serif;
    color: var(--ink);
    position: relative;
  }
  .letterhead {
    position: absolute;
    left: 328px; top: 18px;
    width: 544px; height: 767px;
    background: var(--paper);
    box-shadow: 0 6px 18px rgba(0,0,0,.25);
    overflow: hidden;
  }
  .edge-band {
    position: absolute; left: 0; top: 0; bottom: 0; width: 12px;
    background: var(--brand-blue);
  }
  .base-band {
    position: absolute; left: 0; right: 0; bottom: 0; height: 12px;
    background: var(--brand-blue);
  }
  .footer-panel {
    position: absolute; left: 12px; right: 0; top: 577px; bottom: 12px;
    background: var(--panel);
    border-bottom-left-radius: 12px;
  }
  .masthead {
    position: absolute; left: 12px; right: 0; top: 50px;
    text-align: center;
  }
  .company-name {
    font-weight: 900; font-size: 36px; letter-spacing: -0.5px;
    color: var(--brand-purple); line-height: 1;
  }
  .company-tagline {
    display: flex; align-items: center; justify-content: center; gap: 8px;
    margin-top: 4px;
    font-weight: 700; font-size: 12.5px; letter-spacing: 1px;
    color: var(--muted);
  }
  .company-tagline::before, .company-tagline::after {
    content: ""; width: 48px; height: 1.5px; background: var(--muted);
  }
  .letter-body {
    position: absolute; left: 42px; right: 53px; top: 152px;
    font-size: 9.2px; line-height: 12px;
  }
  .letter-body p { text-align: justify; margin-bottom: 12px; }
  .letter-body .salutation { text-align: left; margin-bottom: 12px; }
  .sign-off {
    position: absolute; left: 42px; top: 563px;
    font-size: 9.2px; line-height: 12px;
  }
  .signature {
    display: block; width: 80px; height: 48px; margin: 4px 0 8px 18px;
    background: linear-gradient(90deg, var(--signature-tone), rgba(230,230,234,0));
    border-radius: 3px;
  }
  .signer-name { font-weight: 700; }
  .footer-rule {
    position: absolute; left: 47px; right: 46px; top: 698px;
    height: 1px; background: var(--rule);
  }
  .contact-row {
    position: absolute; left: 82px; right: 46px; top: 711px;
    display: flex; gap: 18px;
    font-size: 8px; line-height: 11px; color: var(--ink);
  }
  .contact-item { display: flex; align-items: center; gap: 8px; }
  .contact-item svg { width: 14px; height: 14px; flex: none; }
  .contact-item:nth-child(1) { width: 152px; }
  .contact-item:nth-child(2) { width: 92px; }
</style>
</head>
<body>
  <main class="letterhead">
    <div class="footer-panel"></div>
    <div class="edge-band"></div>
    <div class="base-band"></div>

    <header class="masthead">
      <div class="company-name">HALVERN</div>
      <div class="company-tagline">Realty Group, LLC</div>
    </header>

    <section class="letter-body">
      <p class="salutation">Lorem Ipsum is simply</p>
      <p>Dummy text of the printing and typesetting industry. Lorem Ipsum has been the industry's standard dummy text ever since the 1500s, when an unknown printer took a galley of type and scrambled it to make a type specimen book. It has survived not only five centuries, but also the leap into electronic typesetting, remaining essentially unchanged. It was popularised in the 1960s with the release of Typeleaf sheets containing Lorem Ipsum passages, and more recently with desktop publishing software like Pressline Composer including versions of Lorem Ipsum.</p>
      <p>Lorem Ipsum is simply dummy text of the printing and typesetting industry. Lorem Ipsum has been the industry's standard dummy text ever since the 1500s, when an unknown printer took a galley of type and scrambled it to make a type specimen book. It has survived not only five centuries, but also the leap into electronic typesetting, remaining essentially unchanged. It was popularised in the 1960s with the release of Typeleaf sheets containing Lorem Ipsum passages, and more recently with desktop publishing software like Pressline Composer including versions of Lorem Ipsum.</p>
      <p>Lorem Ipsum is simply dummy text of the printing and typesetting industry. Lorem Ipsum has been the industry's standard dummy text ever since the 1500s, when an unknown printer took a galley of type and scrambled it to make a type specimen book. It has survived not only five centuries, but also the leap into electronic typesetting, remaining essentially unchanged. It was popularised in the 1960s with the release of Typeleaf sheets containing Lorem Ipsum passages, and more recently with desktop publishing software like Pressline Composer including versions of Lorem Ipsum.</p>
      <p>Lorem Ipsum is simply dummy text of the printing and typesetting industry. Lorem Ipsum has been the industry's standard dummy text ever since the 1500s, when an unknown printer took a galley of type and scrambled it to make a type specimen book. It has survived not only five centuries, but also the leap into electronic typesetting, remaining essentially unchanged. It was popularised in the 1960s with the release of Typeleaf sheets containing Lorem Ipsum passages, and more recently with desktop publishing software like Pressline Composer including versions of Lorem Ipsum.Lorem Ipsum is simply dummy text of the printing and typesetting industry. Lorem Ipsum has been the industry's standard dummy text ever since the 1500s, when an unknown printer took a galley of type and scrambled it to make a type specimen book.</p>
    </section>

    <section class="sign-off">
      <div>Lorem Ipsum Dummy Text</div>
      <span class="signature" role="img" aria-label="Handwritten signature"></span>
      <div class="signer-name">Lorem Ipsum Dummy Text</div>
    </section>

    <div class="footer-rule"></div>
    <footer class="contact-row">
      <div class="contact-item">
        <svg viewBox="0 0 16 16" fill="none" stroke="#4b2a8c" stroke-width="1.2"><path d="M8 14s-4-4.3-4-7.5a4 4 0 0 1 8 0C12 9.7 8 14 8 14z"/><circle cx="8" cy="6.5" r="1.5"/><path d="M4 14.5h8"/></svg>
        <span>123, Your Address Goes Here,<br>NY, USA- 123456</span>
      </div>
      <div class="contact-item">
        <svg viewBox="0 0 16 16" fill="none" stroke="#4b2a8c" stroke-width="1.2"><circle cx="8" cy="8" r="7"/><path d="M5.5 4.5l1.3 1.8-.8 1c.5 1 1.3 1.8 2.3 2.3l1-.8 1.8 1.3-.8 1.2c-2.6-.3-4.9-2.6-5.2-5.2z"/></svg>
        <span>+0123 456 789<br>+0123 456 789</span>
      </div>
      <div class="contact-item">
        <svg viewBox="0 0 16 16" fill="none" stroke="#4b2a8c" stroke-width="1.2"><circle cx="8" cy="8" r="7"/><ellipse cx="8" cy="8" rx="3" ry="7"/><path d="M1 8h14M2.2 4.5h11.6M2.2 11.5h11.6"/></svg>
        <span>info@yourmailid.com<br>www.yourwebsite.com</span>
      </div>
    </footer>
  </main>
</body>
</html>
```